Sub-Antarctic Islands - Xmas and New Year 2020

I need to create a double sided A4 flyer that I will need to be able to have printed in colour and also email as an attachment.

My company is a Travel agency that packages flights/hotels/transfers&cruise and sells it as one price to the public.

Please see the attachment the email has a lot of info.

Target Market(s)

Bird Watchers

Industry/Entity Type

Travel Industry

Font styles to use
Sans Serif

Colors

Designer to choose colors to be used in the design.

Requirements
Must have
• VoyaMerry Logo
• Goldwake Logo
• Cruise Itinerary
• Inclusions in the package
• Costings
• Photo of one of the bird pictures and a penguin and or a seal
Nice to have
• A very professional appearance.
• A flyer that would make you want to call me to book
• Must be very clear to read as most buyers are seniors
• Please see the attachment the email has a lot of info.
Should not have
• any abbreviations

```html
<!DOCTYPE html>
<html lang="en">
<head>
<meta charset="utf-8">
<title>VoyaMerry – Sub Antarctic Islands Flyer</title>
<link rel="stylesheet" href="https://fonts.googleapis.com/css2?family=Montserrat:wght@400;500;600;700;800&family=Oswald:wght@500;600;700&display=swap">
<style>
  :root{
    --navy:#0f2a5c;
    --blue:#1f4f9e;
    --gold:#c9a24a;
    --gold-dark:#a9832f;
    --snow:#f3f5f8;
    --snow-shade:#d9dee6;
    --ink:#3a4150;
    --canvas:#e9e9ea;
    --white:#ffffff;
  }
  *{box-sizing:border-box;margin:0;padding:0}
  html,body{width:1200px;height:3060px;overflow:hidden;background:var(--canvas)}
  body{font-family:"Montserrat",Arial,sans-serif;color:var(--ink)}
  .page{position:absolute;left:80px;width:1040px;height:1470px;overflow:hidden;box-shadow:0 4px 18px rgba(0,0,0,.12)}
  .page--front{top:40px;background:linear-gradient(180deg,var(--white) 0%,var(--snow) 55%,var(--snow-shade) 100%)}
  .page--back{top:1550px;background:linear-gradient(180deg,var(--navy) 0%,var(--navy) 34%,#dfe5ee 42%,var(--snow) 100%)}

  .brand{display:flex;align-items:center;gap:14px;font-weight:800;font-size:44px;letter-spacing:1px;color:var(--navy)}
  .brand__dot{width:30px;height:30px;background:var(--gold);border-radius:50%}
  .page--back .brand{color:var(--white);justify-content:center}

  /* front */
  .front__brand{position:absolute;left:60px;top:56px}
  .front__title{position:absolute;left:60px;top:160px;color:var(--blue);line-height:1}
  .title__xmas{font-family:"Oswald",sans-serif;font-weight:600;font-size:74px}
  .title__newyear{font-family:"Oswald",sans-serif;font-weight:700;font-size:96px;margin-top:6px}
  .title__year{font-family:"Oswald",sans-serif;font-weight:700;font-size:170px;color:var(--gold);margin-top:4px;letter-spacing:4px}
  .title__dep{font-weight:700;font-size:54px;margin-top:6px}

  .front__photo-frame{position:absolute;right:-40px;top:-20px;width:520px;height:560px;background:var(--navy);clip-path:polygon(22% 0,100% 0,100% 92%,58% 100%,0 58%)}
  .front__photo{position:absolute;right:-40px;top:-20px;width:520px;height:560px;background:linear-gradient(160deg,#cfd6c4 0%,#7f8f6c 45%,#4e5f3d 100%);clip-path:polygon(26% 3%,97% 3%,97% 88%,58% 95%,6% 57%)}

  .columns{position:absolute;left:60px;right:60px;top:640px;display:grid;grid-template-columns:1fr 1fr;gap:50px}
  .bar{background:var(--gold);color:var(--white);font-weight:700;font-size:22px;padding:13px 16px;text-align:center}
  .col__text{font-size:17px;line-height:1.45;margin-top:16px}
  .col__text p{margin-bottom:6px}

  .costing{position:absolute;left:60px;right:60px;top:1080px}
  .costing__band{background:var(--gold);color:var(--white);font-family:"Oswald",sans-serif;font-weight:600;font-size:44px;text-align:center;padding:6px 0}
  .costing__grid{display:grid;grid-template-columns:1fr 1fr;gap:50px;margin-top:18px;font-size:17px;line-height:1.45}
  .costing__grid p{margin-bottom:6px}
  .costing__grid strong{color:var(--navy)}
  .front__email{position:absolute;left:0;right:0;bottom:36px;text-align:center;font-weight:600;font-size:24px;color:var(--navy)}

  /* back */
  .back__brand{position:absolute;left:0;right:0;top:52px}
  .back__headline{position:absolute;left:60px;right:60px;top:150px;text-align:center;font-family:"Oswald",sans-serif;line-height:1.08}
  .headline__main{color:var(--gold);font-weight:700;font-size:70px;text-transform:uppercase}
  .headline__sub{color:var(--white);font-weight:600;font-size:46px;text-transform:uppercase;margin-top:12px;letter-spacing:1px}
  .back__photo{position:absolute;left:60px;right:60px;top:540px;height:500px;background:linear-gradient(180deg,rgba(223,229,238,0) 0%,#c9d1dc 40%,#2b2f38 62%,#f4f6f9 100%);border-radius:4px}
  .back__columns{position:absolute;left:60px;right:60px;top:1070px;display:grid;grid-template-columns:1fr 1fr;gap:50px;font-size:17px;line-height:1.5}
  .back__footer{position:absolute;left:60px;right:60px;bottom:50px;display:grid;grid-template-columns:1fr 1fr;gap:50px;align-items:end}
  .footer__label{font-weight:700;font-size:26px;color:var(--gold-dark);text-transform:uppercase}
  .footer__phone{font-family:"Oswald",sans-serif;font-weight:600;font-size:64px;color:var(--navy);line-height:1.05;white-space:nowrap}
  .footer__email{font-weight:600;font-size:24px;color:var(--navy);border-left:3px solid var(--gold);padding-left:24px}
  .footer__email span{display:block;font-size:19px;color:var(--gold-dark);font-weight:700;margin-bottom:6px}
</style>
</head>
<body>

<section class="page page--front">
  <div class="front__photo-frame"></div>
  <div class="front__photo" role="img" aria-label="Photograph of a pair of albatrosses on a grassy island slope"></div>

  <div class="brand front__brand"><span class="brand__dot"></span>VoyaMerry</div>

  <div class="front__title">
    <div class="title__xmas">Xmas and</div>
    <div class="title__newyear">NEW YEAR</div>
    <div class="title__year">2020</div>
    <div class="title__dep">New Departure</div>
  </div>

  <div class="columns">
    <div class="col">
      <div class="bar">VoyaMerry Special Itinerary</div>
      <div class="col__text">
        <p>Day 1 Fly from Sydney to Invercargill and transfer to your hotel.</p>
        <p>Day 2 Board Goldwake in Bluff and sail toward the Snares Islands.</p>
        <p>Days 3 to 5 Auckland Islands guided landings and bird walks.</p>
        <p>Days 6 to 8 Macquarie Island penguins and elephant seals.</p>
        <p>Days 9 to 11 Campbell Island albatross nesting grounds.</p>
        <p>Day 12 Return to Bluff and fly home to Sydney.</p>
      </div>
    </div>
    <div class="col">
      <div class="bar">VoyaMerry Package Inclusions</div>
      <div class="col__text">
        <p>Return economy flights from Sydney to Invercargill with all taxes.</p>
        <p>One night hotel stay in Invercargill with breakfast.</p>
        <p>Private transfers between airport, hotel and ship.</p>
        <p>Twelve night expedition cruise in a veranda suite.</p>
        <p>All meals, drinks and guided shore landings.</p>
        <p>Expedition parka to keep.</p>
      </div>
    </div>
  </div>

  <div class="costing">
    <div class="costing__band">Costing</div>
    <div class="costing__grid">
      <div>
        <p><strong>$9,995</strong> per person sharing a veranda suite</p>
        <p><strong>$14,500</strong> single traveller in a veranda suite</p>
        <p>Deposit of <strong>$2,000</strong> per person due within seven days of booking</p>
        <p>Final payment due ninety days before departure</p>
      </div>
      <div>
        <p>Price valid for bookings made on or before <strong>30 June 2019</strong></p>
        <p>All payments made by bank transfer or credit card</p>
      </div>
    </div>
  </div>

  <div class="front__email">bookings@voyamerry.com.au</div>
</section>

<section class="page page--back">
  <div class="brand back__brand"><span class="brand__dot"></span>VoyaMerry</div>

  <div class="back__headline">
    <div class="headline__main">Bird Watching at<br>Macquarie Island and<br>the New Zealand</div>
    <div class="headline__sub">Sub Antarctic Islands Expedition</div>
  </div>

  <div class="back__photo" role="img" aria-label="Photograph of crested penguins walking across snow"></div>

  <div class="back__columns">
    <p>A unique journey with Goldwake to the remote islands south of New Zealand, home to rare seabirds and penguins found nowhere else. Sail in comfort with expert naturalists.</p>
    <p>Walk among royal and king penguin colonies, watch elephant seals on the beaches and see wandering albatross soar. Places are limited, so book early.</p>
  </div>

  <div class="back__footer">
    <div>
      <div class="footer__label">Call us now</div>
      <div class="footer__phone">1-300-555-014</div>
    </div>
    <div class="footer__email"><span>Enquire by email</span>bookings@voyamerry.com.au</div>
  </div>
</section>

</body>
</html>
```